Need a plumber

Would like a postcard sized flyer made up. Want the design to be kept very simple.
List of services we carry out in bullet point or similar.
Phone number and email included on the flyer.
Logo to feature prominantly.

List of services: Hot water issues
Burst Pipes
Gas Plumbing
Roof leaks
Drain blockages

Target Market(s)

Mums, dads and hosehgold owners

Industry/Entity Type

Plumbing

Colors
0054AA
0677BA
7BADD7
CADEEF
E8F1F8

Requirements
Must have
• Services we off and our logo, also must say "local plumber"

```html
<!DOCTYPE html>
<html lang="en">
<head>
<meta charset="utf-8">
<title>Plumbing Services Flyer</title>
<link rel="stylesheet" href="https://fonts.googleapis.com/css2?family=Dosis:wght@400;600;700;800&display=swap">
<style>
  :root {
    --canvas: #f3f3f1;
    --paper: #d6e8ee;
    --art-light: #8cbfe6;
    --art-dark: #5f9dcf;
    --navy: #24476a;
    --bullet: #4f90c2;
    --badge: #0b0b0c;
    --ring: #4b8fcf;
    --white: #ffffff;
  }
  * { margin: 0; padding: 0; box-sizing: border-box; }
  html, body { width: 1200px; height: 801px; overflow: hidden; background: var(--canvas); }
  body { position: relative; font-family: "Dosis", sans-serif; color: var(--navy); }

  .flyer {
    position: absolute; left: 336px; top: 20px;
    width: 527px; height: 761px;
    background: var(--paper);
    overflow: hidden;
  }
  .flyer-art { position: absolute; inset: 0; width: 527px; height: 761px; }

  .headline {
    position: absolute; left: 180px; top: 26px; width: 320px;
    font-weight: 800; font-size: 62px; line-height: 68px; letter-spacing: 0.5px;
    color: var(--navy);
  }

  .services { position: absolute; left: 56px; top: 314px; list-style: none; }
  .services li {
    display: flex; align-items: center; height: 36.5px;
    font-weight: 700; font-size: 16.5px; letter-spacing: 0.2px;
  }
  .services li::before {
    content: ""; width: 9px; height: 12px; margin-right: 13px;
    background: var(--bullet);
    border-radius: 50% 50% 50% 50% / 40% 40% 60% 60%;
  }

  .local-badge {
    position: absolute; left: 216px; top: 326px; width: 110px; height: 110px;
    display: flex; align-items: center; justify-content: center; text-align: center;
    font-weight: 700; font-size: 18px; line-height: 18px; color: var(--white);
  }

  .brand {
    position: absolute; left: 323px; top: 500px; width: 180px; height: 180px;
    display: flex; align-items: center; justify-content: center;
    text-align: center; color: var(--white);
    font-weight: 700; font-size: 18px; line-height: 24px; letter-spacing: 3px;
  }

  .contact { position: absolute; left: 140px; top: 654px; }
  .contact-row { display: flex; align-items: center; gap: 13px; }
  .contact-row svg { flex: none; }
  .contact-phone { font-weight: 700; font-size: 21px; height: 30px; }
  .contact-small { font-weight: 400; font-size: 11.5px; height: 28px; }
</style>
</head>
<body>
<main class="flyer">
  <svg class="flyer-art" viewBox="0 0 527 761">
    <defs>
      <linearGradient id="art-tone" x1="0" y1="0" x2="1" y2="1">
        <stop offset="0" stop-color="var(--art-light)"/>
        <stop offset="1" stop-color="var(--art-dark)"/>
      </linearGradient>
    </defs>

    <g class="pipe-illustration" role="img" aria-label="Illustration of blue water pipes with a valve wheel, a cracked leaking section, a tap and falling water drops" fill="url(#art-tone)">
      <rect x="38" y="0" width="100" height="292" rx="20"/>
      <rect x="38" y="200" width="462" height="90" rx="20"/>
      <rect x="352" y="200" width="148" height="360" rx="20"/>
      <rect x="36" y="520" width="300" height="130" rx="20"/>
      <rect x="46" y="650" width="76" height="100" rx="24"/>
    </g>

    <circle cx="271" cy="381" r="60" fill="var(--paper)" stroke="var(--badge)" stroke-width="1"/>
    <circle cx="271" cy="381" r="55" fill="var(--badge)"/>
    <circle cx="271" cy="381" r="47" fill="none" stroke="var(--ring)" stroke-width="1"/>

    <circle cx="413" cy="590" r="92" fill="var(--badge)"/>
  </svg>

  <h1 class="headline">PLUMBING<br>SERVICES</h1>

  <ul class="services">
    <li>HOT WATER ISSUES</li>
    <li>BURST PIPES</li>
    <li>GAS PLUMBING</li>
    <li>ROOF LEAKS</li>
    <li>DRAIN BLOCKAGE</li>
  </ul>

  <div class="local-badge">LOCAL<br>PLUMBER</div>

  <div class="brand">CLEARFLOW<br>PLUMBING</div>

  <div class="contact">
    <div class="contact-row contact-phone">
      <svg width="16" height="16" viewBox="0 0 16 16" aria-hidden="true">
        <circle cx="8" cy="8" r="8" fill="var(--navy)"/>
        <path d="M5.2,4 L6.8,4 L7.4,6 L6.5,6.8 Q7.3,8.6 9.2,9.5 L10,8.6 L12,9.2 L12,10.8 Q11.6,12 10.4,12 Q6.8,11.6 4.4,7.8 Q4,5 5.2,4Z" fill="var(--white)"/>
      </svg>
      <span>+61 400 218 375</span>
    </div>
    <div class="contact-row contact-small">
      <svg width="16" height="16" viewBox="0 0 16 16" aria-hidden="true">
        <circle cx="8" cy="8" r="8" fill="var(--navy)"/>
        <rect x="4" y="5" width="8" height="6" rx="0.8" fill="none" stroke="var(--white)" stroke-width="1.2"/>
        <path d="M4.3,5.4 L8,8.3 L11.7,5.4" fill="none" stroke="var(--white)" stroke-width="1.2"/>
      </svg>
      <span>sam@clearflowplumb.com</span>
    </div>
    <div class="contact-row contact-small">
      <svg width="16" height="16" viewBox="0 0 16 16" aria-hidden="true">
        <circle cx="8" cy="8" r="8" fill="var(--navy)"/>
        <path d="M8,3.5 Q11,3.5 11,6.5 Q11,8.5 8,12.5 Q5,8.5 5,6.5 Q5,3.5 8,3.5Z" fill="var(--white)"/>
        <circle cx="8" cy="6.6" r="1.2" fill="var(--navy)"/>
      </svg>
      <span>Bayview Heights, VIC, Australia, Victoria</span>
    </div>
  </div>
</main>
</body>
</html>
```